Stanbrook Fire Services Pty Ltd

We need business cards for a company based in Perth, we install, service and maintain fire equipment.
On the front we want a great design with our logo and a small spot for our full company name, general company email address and office number. On the back we need space for our name, title, mobile number and email address on the back.

Target Market(s)

Facility managers and commercial/industrial building owners/occupiers.

Contact Information for Business Card

Font styles to use
Sans Serif

Requirements
Must have
• Please only submit 5 of your best samples.
Darker tones are preferred.
Nice to have
• We want to use, black, red and grey. Keep it modern and clean.
I've attached the company logo and a sample of a boarder we use on our emergency plans.
Should not have
• No preference. Let the designer choose.

```html
<!DOCTYPE html>
<html lang="en">
<head>
<meta charset="utf-8">
<title>Stanbrook Fire Services – Business Cards</title>
<link href="https://fonts.googleapis.com/css2?family=Montserrat:wght@400;500;700;800&display=swap" rel="stylesheet">
<style>
  :root {
    --page-bg: #3a3a3a;
    --card-black: #0c0c0d;
    --brand-red: #ec1c24;
    --brand-grey: #8a8a8c;
    --text-white: #f4f4f4;
  }
  * { box-sizing: border-box; margin: 0; padding: 0; }
  html, body {
    width: 1200px; height: 900px; overflow: hidden;
    background: var(--page-bg);
    font-family: 'Montserrat', sans-serif;
  }
  .sheet {
    width: 1200px; height: 900px;
    display: flex; flex-direction: column; align-items: center; justify-content: center;
    gap: 40px;
  }
  .card {
    position: relative;
    width: 630px; height: 360px;
    background: var(--card-black);
    box-shadow: 0 14px 30px rgba(0,0,0,.45);
    overflow: hidden;
  }

  /* Front */
  .front__brand {
    position: absolute; top: 88px; left: 0; right: 0;
    text-align: center;
    font-size: 58px; font-weight: 800; letter-spacing: 2px;
    color: var(--brand-grey);
  }
  .front__web {
    position: absolute; top: 218px; right: 150px;
    font-size: 14px; font-weight: 500; color: var(--brand-red);
  }
  .front__band {
    position: absolute; left: 0; right: 0; top: 248px; height: 40px;
    background: var(--brand-red);
    display: flex; align-items: center; justify-content: center; gap: 22px;
    color: var(--text-white); font-size: 12.5px; font-weight: 500;
  }
  .band-item { display: flex; align-items: center; gap: 6px; white-space: nowrap; }
  .icon { width: 12px; height: 12px; flex: none; }

  /* Back */
  .back__brand {
    position: absolute; left: 70px; top: 152px;
    font-size: 40px; font-weight: 800; letter-spacing: 1px;
    color: var(--brand-red);
  }
  .back__divider {
    position: absolute; left: 352px; top: 92px; width: 2px; height: 150px;
    background: var(--brand-red);
  }
  .back__details {
    position: absolute; left: 378px; top: 100px;
    color: var(--text-white);
  }
  .person__name {
    font-size: 21px; font-weight: 800; letter-spacing: 1.5px;
    color: var(--brand-red); text-transform: uppercase;
  }
  .person__title { font-size: 15px; font-weight: 400; margin-top: 2px; }
  .contact-list { list-style: none; margin-top: 16px; font-size: 12.5px; }
  .contact-list li { display: flex; align-items: center; gap: 8px; margin-bottom: 6px; }
  .back__edge {
    position: absolute; left: 0; right: 0; bottom: 0; height: 7px;
    background: var(--brand-red);
  }
</style>
</head>
<body>
<main class="sheet">

  <section class="card card--front" aria-label="Business card front">
    <div class="front__brand">STANBROOK</div>
    <div class="front__web">www.stanbrookfire.com.au</div>
    <div class="front__band">
      <span class="band-item">
        <svg class="icon" viewBox="0 0 24 24" fill="#fff"><path d="M6.6 10.8a15 15 0 0 0 6.6 6.6l2.2-2.2c.3-.3.7-.4 1-.2 1.1.4 2.3.6 3.6.6.6 0 1 .4 1 1V20c0 .6-.4 1-1 1A17 17 0 0 1 3 4c0-.6.4-1 1-1h3.5c.6 0 1 .4 1 1 0 1.3.2 2.5.6 3.6.1.3 0 .7-.2 1z"/></svg>
        (08) 9321 4470
      </span>
      <span class="band-item">
        <svg class="icon" viewBox="0 0 24 24" fill="#fff"><path d="M2 5h20v14H2z"/><path d="M2 5l10 8 10-8" stroke="#ec1c24" stroke-width="2" fill="none"/></svg>
        contact@stanbrookfire.com.au
      </span>
      <span class="band-item">
        <svg class="icon" viewBox="0 0 24 24" fill="#fff"><path d="M12 2a7 7 0 0 0-7 7c0 5 7 13 7 13s7-8 7-13a7 7 0 0 0-7-7zm0 9.5A2.5 2.5 0 1 1 12 6.5a2.5 2.5 0 0 1 0 5z"/></svg>
        48 Kembla Road, Perth WA 6000
      </span>
    </div>
  </section>

  <section class="card card--back" aria-label="Business card back">
    <div class="back__brand">STANBROOK</div>
    <div class="back__divider"></div>
    <div class="back__details">
      <div class="person__name">Daniel Hart</div>
      <div class="person__title">Owner</div>
      <ul class="contact-list">
        <li>
          <svg class="icon" viewBox="0 0 24 24" fill="#ec1c24"><path d="M6.6 10.8a15 15 0 0 0 6.6 6.6l2.2-2.2c.3-.3.7-.4 1-.2 1.1.4 2.3.6 3.6.6.6 0 1 .4 1 1V20c0 .6-.4 1-1 1A17 17 0 0 1 3 4c0-.6.4-1 1-1h3.5c.6 0 1 .4 1 1 0 1.3.2 2.5.6 3.6.1.3 0 .7-.2 1z"/></svg>
          0412 558 931
        </li>
        <li>
          <svg class="icon" viewBox="0 0 24 24" fill="#ec1c24"><path d="M2 5h20v14H2z"/><path d="M2 5l10 8 10-8" stroke="#0c0c0d" stroke-width="2" fill="none"/></svg>
          daniel@stanbrookfire.com.au
        </li>
        <li>
          <svg class="icon" viewBox="0 0 24 24"><circle cx="12" cy="12" r="10" fill="#ec1c24"/><path d="M2 12h20M12 2c3 3 3 17 0 20M12 2c-3 3-3 17 0 20" stroke="#0c0c0d" stroke-width="1.5" fill="none"/></svg>
          www.stanbrookfire.com.au
        </li>
      </ul>
    </div>
    <div class="back__edge"></div>
  </section>

</main>
</body>
</html>
```